Family Office for small businesses needs clear web site

I founded VORUSK Family Office, which is a french family office design to change the relationship between the customer and the wealth manager/insurance broker.
The main focus is : we give back to the client all the commissions / hidden costs we gain from the insurance companies / real estate builders and we bill to the client an annual fee proportional to the wealth. Thus a transparent relationship exempt from conflict of interest

I want a WORPRESS theme design that will be easily customizable in the future. Using and existing wordpress theme is not a problem, as long as i get to customize it in the future if necessary.
I want the web site to be Simple, clear, explaining the concepts detailed in the word doc i join to this project
In the chart are some of the things we do (not all, but most).
Also i joined some question a client might ask himself before calling us

i am available to clarify any issue or concepts

Reason: I want to let new designer submit their proposal. I really wish to conclude this design contest to move forward on other projects.

Target Market(s)

small businesses, specically their boss

Industry/Entity Type

Office

Number of Pages Required

1 page

Font styles to use
Serif

Colors
85acd3
3176b5
0455a3
cedeed
eaf1f7
cee9f5
85cae6
33a6d7
0692cd

Requirements
Must have
• I would like to have a one page wordpress theme personalized by a designer.
• I don't really care if you use an existing wordpress theme, as long as it can be upgraded/customized later on using wordpress/admin.
• I can even provide some themes I bought if it can help maintain the budget..
• O I can pay additional fee for a theme you bought to provide the design..

```html
<!DOCTYPE html>
<html lang="en">
<head>
<meta charset="utf-8">
<title>VORUSK Family Office</title>
<link href="https://fonts.googleapis.com/css2?family=Open+Sans:wght@300;400;600;700&display=swap" rel="stylesheet">
<style>
:root{
  --blue-soft:#85acd3;
  --blue-mid:#3176b5;
  --blue-deep:#0455a3;
  --blue-pale:#cedeed;
  --blue-mist:#eaf1f7;
  --sky-pale:#cee9f5;
  --sky-light:#85cae6;
  --sky:#33a6d7;
  --sky-strong:#0692cd;
  --navy:#123a66;
  --ink:#44505c;
  --white:#ffffff;
}
*{box-sizing:border-box;margin:0;padding:0}
html,body{width:1200px;height:2216px;overflow:hidden}
body{font-family:"Open Sans",Arial,sans-serif;color:var(--ink);background:var(--white);font-size:13px;line-height:1.55}
.page{width:1200px;height:2216px;position:relative}

/* header */
.site-header{height:64px;display:flex;align-items:center;justify-content:space-between;padding:0 96px 0 110px;background:var(--white);box-shadow:0 2px 6px rgba(0,0,0,.08);position:relative;z-index:2}
.brand-name{font-size:19px;font-weight:700;letter-spacing:.5px;line-height:1;color:var(--navy);text-transform:uppercase}
.main-nav{display:flex;align-items:center;gap:30px;font-size:12px;color:var(--ink)}
.main-nav .active{color:var(--sky-strong);font-weight:600}
.search{width:100px;height:24px;border:1px solid var(--blue-pale);font-size:11px;padding:3px 8px;color:#9aa}

/* hero */
.hero{height:356px;position:relative;background:linear-gradient(160deg,#4d7396 0%,#6e8fa9 35%,#a9bccb 60%,#58799a 100%)}
.hero-photo{position:absolute;inset:0}
.hero-text{position:absolute;left:0;right:0;top:200px;text-align:center;color:var(--white);font-weight:300;font-size:30px;line-height:1.2;text-shadow:0 1px 3px rgba(0,0,0,.3)}

/* welcome */
.welcome{height:370px;background:linear-gradient(180deg,var(--blue-mist),var(--white));padding:36px 96px;display:flex;gap:30px}
.welcome-box{flex:0 0 600px;background:var(--sky-strong);color:var(--white);padding:26px 30px}
.welcome-box h2{font-size:23px;font-weight:600;margin-bottom:16px}
.welcome-box p{font-size:12px;margin-bottom:12px;color:var(--sky-pale)}
.mind-map{flex:1;background:linear-gradient(135deg,var(--blue-mist),var(--blue-pale));border-radius:4px}

/* services */
.services{height:300px;background:var(--blue-mist);padding:14px 96px 0;display:flex;gap:18px}
.service-card{flex:1;background:var(--white);box-shadow:0 1px 4px rgba(0,0,0,.12);text-align:center;height:270px}
.service-photo{height:110px;background:linear-gradient(135deg,var(--blue-soft),var(--blue-pale))}
.service-card h3{font-size:14px;font-weight:600;color:var(--navy);margin:12px 10px 8px;line-height:1.25}
.service-card p{font-size:10.5px;padding:0 18px;color:#7a8590}
.learn-more{display:block;margin-top:8px;font-size:11px;font-weight:600;color:var(--blue-mid)}

/* expertise band */
.expertise{height:340px;background:linear-gradient(180deg,var(--blue-mid),var(--blue-deep));color:var(--white);text-align:center;padding:44px 150px 0}
.expertise h2{font-size:24px;font-weight:600;margin-bottom:18px}
.expertise p{font-size:12px;color:var(--sky-pale);margin-bottom:10px}
.btn{display:inline-block;margin-top:18px;padding:8px 20px;border:1px solid var(--sky-light);background:var(--sky-strong);color:var(--white);font-size:12px}

/* values */
.values{height:330px;background:var(--white);text-align:center;padding-top:40px}
.values h2{font-size:24px;font-weight:600;color:var(--blue-deep);line-height:1.3}
.value-list{display:flex;justify-content:center;gap:140px;margin-top:36px}
.value{width:130px}
.value-icon{width:100px;height:100px;border-radius:50%;background:var(--blue-mid);margin:0 auto 14px;display:flex;align-items:center;justify-content:center}
.value span{font-size:12px;color:var(--blue-mid);font-weight:600;text-transform:uppercase}

/* testimonials */
.testimonials{height:250px;background:linear-gradient(180deg,#2a5f8f,#184a7a);color:var(--white);text-align:center;padding-top:26px}
.avatar{width:70px;height:70px;border-radius:50%;border:3px solid var(--white);background:linear-gradient(135deg,var(--blue-soft),var(--blue-mid));margin:0 auto 8px}
.testimonials h2{font-size:20px;font-weight:300;margin-bottom:10px}
.testimonials p{font-size:12px;color:var(--sky-pale);width:680px;margin:0 auto}

/* footer */
.site-footer{height:166px;background:var(--navy);color:var(--white);display:flex;padding:30px 96px 0;gap:50px}
.footer-brand{flex:0 0 300px}
.footer-brand .brand-name{color:var(--white)}
.footer-col{flex:1}
.footer-col h4{font-size:14px;font-weight:600;margin-bottom:8px}
.footer-col p{font-size:10.5px;color:var(--blue-soft)}
.social{display:flex;gap:8px;margin-top:10px}
.social i{width:22px;height:22px;background:var(--sky-strong);display:block}
.share-row{display:flex;gap:6px;margin-top:10px}
.share-input{flex:1;height:26px;background:var(--white);font-size:10px;color:#99a;padding:5px 8px}
.share-btn{height:26px;padding:5px 14px;background:var(--sky-strong);font-size:11px}
.bottom-bar{height:40px;background:#0c2c50;color:var(--blue-soft);display:flex;align-items:center;justify-content:space-between;padding:0 96px;font-size:11px}
.bottom-nav{display:flex;gap:26px}
</style>
</head>
<body>
<div class="page">
  <header class="site-header">
    <div class="brand"><span class="brand-name">VORUSK Family Office</span></div>
    <nav class="main-nav">
      <span class="active">Home</span><span>About us</span><span>Projects</span><span>Services</span><span>Blog</span><span>Contacts</span>
      <span class="search">Search</span>
    </nav>
  </header>

  <section class="hero">
    <div class="hero-photo" role="img" aria-label="Photo of a couple relaxing together at home, soft blue tones"></div>
    <div class="hero-text">FAMILY OFFICE: Vorusk is a family office.<br>A Family Office is a consultancy wealth management.<br>that acts in your interest only.</div>
  </section>

  <section class="welcome">
    <div class="welcome-box">
      <h2>Welcome to wealth management consultancy</h2>
      <p>We help business owners organise their private and professional wealth with one clear view. Every decision is taken with you, explained simply, and followed over time so your family goals stay on track through each stage of life.</p>
      <p>We return every commission received from insurers and builders to you. Our fee is a transparent annual share of the wealth we manage, so our only interest is yours and no hidden cost stands between us and you.</p>
    </div>
    <div class="mind-map" role="img" aria-label="Diagram of the family office services linked around a central node"></div>
  </section>

  <section class="services">
    <article class="service-card">
      <div class="service-photo" role="img" aria-label="Photo of a financial consultant at a desk"></div>
      <h3>Consulting &amp;<br>financial investment</h3>
      <p>We build an investment plan suited to your profile, review it each year and adjust it with you.</p>
      <span class="learn-more">Learn More »</span>
    </article>
    <article class="service-card">
      <div class="service-photo" role="img" aria-label="Photo of insurance documents"></div>
      <h3>Insurance Brokerage</h3>
      <p>We compare contracts across insurers and pass every commission back to you in full, with no exceptions.</p>
      <span class="learn-more">Learn More »</span>
    </article>
    <article class="service-card">
      <div class="service-photo" role="img" aria-label="Photo of a modern residential building"></div>
      <h3>Advising on real estate<br>&amp; Unlisted companies</h3>
      <p>We select property and private company projects and negotiate terms on your behalf alone.</p>
      <span class="learn-more">Learn More »</span>
    </article>
    <article class="service-card">
      <div class="service-photo" role="img" aria-label="Photo of a legal advisor signing papers"></div>
      <h3>Legal &amp; Tax support</h3>
      <p>We coordinate lawyers and notaries to protect your estate and prepare a smooth succession.</p>
      <span class="learn-more">Learn More »</span>
    </article>
  </section>

  <section class="expertise">
    <h2>WEALTH MANAGEMENT, OR LEGAL ASPECTS, TAX AND SUCCESSION</h2>
    <p>Wealth is a whole: your savings, your company, your home and your family. We look at every part together so that one choice never weakens another, and we explain each step in plain words before you decide anything.</p>
    <p>Our approach in terms of wealth management brings clarity, independence and long term follow up. We work with trusted lawyers, tax experts and notaries, and we report to you each year on results, costs and the next steps for your estate, your retirement and the transfer of your business.</p>
    <span class="btn">Read More</span>
  </section>

  <section class="values">
    <h2>OUR ADDED VALUE IS THE RESULT OF<br>A DOUBLE COMMITMENT</h2>
    <div class="value-list">
      <div class="value">
        <div class="value-icon">
          <svg width="50" height="50" viewBox="0 0 50 50"><text x="25" y="38" text-anchor="middle" font-family="Open Sans,Arial,sans-serif" font-size="40" font-weight="600" fill="#fff">$</text></svg>
        </div>
        <span>Earn money</span>
      </div>
      <div class="value">
        <div class="value-icon">
          <svg width="54" height="54" viewBox="0 0 54 54" fill="none" stroke="#fff" stroke-width="4"><circle cx="27" cy="27" r="22"/><circle cx="27" cy="27" r="13"/><circle cx="27" cy="27" r="4" fill="#fff"/></svg>
        </div>
        <span>Life easier</span>
      </div>
      <div class="value">
        <div class="value-icon">
          <svg width="58" height="48" viewBox="0 0 58 48" fill="#fff"><circle cx="29" cy="14" r="8"/><path d="M15 44c0-10 6-16 14-16s14 6 14 16z"/><circle cx="12" cy="18" r="6"/><path d="M1 42c0-8 5-12 11-12 3 0 5 1 6 2-3 3-5 6-5 10z"/><circle cx="46" cy="18" r="6"/><path d="M57 42c0-8-5-12-11-12-3 0-5 1-6 2 3 3 5 6 5 10z"/></svg>
        </div>
        <span>Efficiency<br>sustainability</span>
      </div>
    </div>
  </section>

  <section class="testimonials">
    <div class="avatar" role="img" aria-label="Client portrait"></div>
    <h2>Testimonials</h2>
    <p>They helped me see my whole estate clearly for the first time. Every fee is visible, every commission came back to us, and our family now has a plan for the company and for retirement that we truly understand.</p>
  </section>

  <footer class="site-footer">
    <div class="footer-brand">
      <span class="brand-name">VORUSK Family Office</span>
    </div>
    <div class="footer-col">
      <h4>Get Social with us</h4>
      <p>Follow our news, advice and events.<br>Join the conversation with our team.</p>
      <div class="social"><i></i><i></i><i></i><i></i><i></i><i></i></div>
    </div>
    <div class="footer-col">
      <h4>Share your thoughts</h4>
      <p>Send us a question or a comment.<br>We reply to every message quickly.</p>
      <div class="share-row"><span class="share-input">Your message</span><span class="share-btn">Send</span></div>
    </div>
  </footer>
  <div class="bottom-bar">
    <nav class="bottom-nav"><span>Home</span><span>About</span><span>Service</span><span>Projects</span><span>Blog</span><span>Contacts</span></nav>
    <span>Copyright © VORUSK Family Office. All rights reserved.</span>
  </div>
</div>
</body>
</html>
```